Wolkrat

I need a design of house and to fill it with art and music and education activities. My project is about a culture house will have many activities. During my presentation, I will name an activity and talk about. each activity will be represented by a person. the last slide I remove the house and leave the figures without a house.. asking the audiences to help to provide the house. the presentation shouldn’t be more than 3 slides. My Pichting is 3 minutes only.

```html
<!DOCTYPE html>
<html lang="en">
<head>
<meta charset="utf-8">
<title>Wolkrat – Culture House</title>
<link href="https://fonts.googleapis.com/css2?family=Quicksand:wght@400;500;600;700&display=swap" rel="stylesheet">
<style>
  :root {
    --red: #e3262b;
    --green: #1f7a3f;
    --green-dark: #15602f;
    --ink: #0b0b0c;
    --band: #d1d2d4;
    --text: #2c2c2c;
    --mark-grey: #4e4f52;
  }
  * { margin: 0; padding: 0; box-sizing: border-box; }
  html, body { width: 1200px; height: 2200px; overflow: hidden; background: #fff; }
  .canvas { position: relative; width: 1200px; height: 2200px; font-family: "Quicksand", sans-serif; color: var(--text); }
  .layer { position: absolute; left: 0; top: 0; }

  /* Title slide */
  .hero-photo {
    position: absolute; left: 27px; top: 30px; width: 1146px; height: 615px;
    background:
      linear-gradient(180deg, rgba(150,154,160,0.55) 0%, rgba(230,232,235,0.2) 18%, rgba(255,255,255,0) 45%, rgba(205,208,212,0.35) 80%, rgba(190,193,198,0.5) 100%),
      linear-gradient(90deg, #b4b8bd 0%, #d9dbde 25%, #e8e9eb 45%, #dfe1e4 49.6%, #e9ecf0 49.7%, #f1f3f6 75%, #e6e9ee 100%);
  }
  .hero-mark {
    position: absolute; left: 690px; top: 372px;
    font-family: "Quicksand", sans-serif; font-weight: 500; font-size: 96px; line-height: 1;
    color: var(--mark-grey); letter-spacing: -1px;
  }

  .divider-band { position: absolute; left: 0; width: 1200px; height: 81px; background: var(--band); }
  .divider-band.first { top: 675px; }
  .divider-band.second { top: 1431px; }

  .house-name {
    position: absolute; left: 0; width: 1200px; text-align: center;
    font-family: "Quicksand", sans-serif; font-weight: 500; font-size: 60px; line-height: 1; color: var(--ink);
  }

  /* Activity cards */
  .activity-card { position: absolute; width: 320px; height: 214px; }
  .activity-photo { position: absolute; inset: 0; }
  .photo-gallery {
    background:
      linear-gradient(180deg, #8f9296 0%, #c9cbce 22%, #eeeff0 45%, #e2e3e5 62%, #f2f2f3 78%, #c6c7c9 100%);
  }
  .photo-culture {
    background:
      linear-gradient(180deg, rgba(255,255,255,0.25) 0%, rgba(255,255,255,0) 40%, rgba(200,202,204,0.4) 100%),
      linear-gradient(100deg, #d6d9db 0%, #5f5d59 22%, #565554 40%, #6e5a4a 58%, #c9cbcd 74%, #eceeef 100%);
  }
  .photo-library {
    background:
      repeating-linear-gradient(180deg, #e5ebef 0px, #e5ebef 14px, #b8c3cc 14px, #b8c3cc 42px),
      #cdd6dd;
  }
  .activity-label {
    position: absolute; left: 0; bottom: 0; width: 100%; height: 38px;
    background: linear-gradient(90deg, var(--green-dark), var(--green) 50%, var(--green-dark));
    color: #fff; font-family: "Quicksand", sans-serif; font-weight: 600; font-size: 19.5px;
    line-height: 38px; padding-left: 17px; white-space: nowrap;
  }

  /* Radio */
  .radio-dot {
    position: absolute; left: 584px; top: 1278px; width: 32px; height: 32px;
    border-radius: 50%; background: var(--green);
  }
  .radio-name {
    position: absolute; left: 0; top: 1320px; width: 1200px; text-align: center;
    font-family: "Quicksand", sans-serif; font-weight: 700; font-size: 23px; color: var(--red);
  }

  /* Activity details */
  .activity-list {
    position: absolute; top: 1931px; width: 305px; list-style: none;
    font-size: 12px; line-height: 13.7px; font-weight: 500; color: var(--text);
  }
  .activity-list li { position: relative; padding-left: 8px; margin-bottom: 12.8px; }
  .activity-list li::before {
    content: ""; position: absolute; left: 0; top: 5px; width: 3px; height: 3px;
    border-radius: 50%; background: var(--red);
  }
</style>
</head>
<body>
<div class="canvas">

  <!-- Title slide -->
  <svg class="layer" width="1200" height="700" aria-hidden="true">
    <polygon points="534,0 1200,0 1200,675 421,675" fill="var(--red)"/>
  </svg>
  <div class="hero-photo" role="img" aria-label="Bright white office corridor with dark doors and a tall window, a white wall on the right carrying the name"></div>
  <div class="hero-mark">Wolkrat</div>

  <div class="divider-band first"></div>

  <!-- House outlines -->
  <svg class="layer" width="1200" height="2200" aria-hidden="true">
    <polyline points="1145,1110 1145,912 601,784 58,912 58,1381 1145,1381"
              fill="none" stroke="var(--ink)" stroke-width="26" stroke-linejoin="miter"/>
    <polyline points="1145,1864 1145,1666 601,1539 58,1666 58,2135 1145,2135"
              fill="none" stroke="var(--ink)" stroke-width="26" stroke-linejoin="miter"/>
  </svg>

  <!-- House one: activities -->
  <div class="house-name" style="top:890px;">Wolkrat</div>

  <div class="activity-card" style="left:96px; top:1005px;">
    <div class="activity-photo photo-gallery" role="img" aria-label="White gallery wall with a row of framed photographs and a bronze bust"></div>
    <div class="activity-label">Art Gallery Cafe(AGC)</div>
  </div>
  <div class="activity-card" style="left:440px; top:1005px;">
    <div class="activity-photo photo-culture" role="img" aria-label="White museum hall with a large curved rusted steel sculpture"></div>
    <div class="activity-label">Thaqafa Culture Centre(TCC)</div>
  </div>
  <div class="activity-card" style="left:792px; top:1005px;">
    <div class="activity-photo photo-library" role="img" aria-label="Multi-level white library atrium with shelves of books and stairways"></div>
    <div class="activity-label">Education Centre Library(ECL)</div>
  </div>

  <div class="radio-dot"></div>
  <div class="radio-name">Levant Alps House Radio</div>

  <div class="divider-band second"></div>

  <!-- House two: activities with details -->
  <div class="house-name" style="top:1598px;">Wolkrat</div>

  <div class="activity-card" style="left:96px; top:1710px;">
    <div class="activity-photo photo-gallery" role="img" aria-label="White gallery wall with a row of framed photographs and a bronze bust"></div>
    <div class="activity-label">Art Gallery Cafe(AGC)</div>
  </div>
  <div class="activity-card" style="left:440px; top:1710px;">
    <div class="activity-photo photo-culture" role="img" aria-label="White museum hall with a large curved rusted steel sculpture"></div>
    <div class="activity-label">Thaqafa Culture Centre(TCC)</div>
  </div>
  <div class="activity-card" style="left:792px; top:1710px;">
    <div class="activity-photo photo-library" role="img" aria-label="Multi-level white library atrium with shelves of books and stairways"></div>
    <div class="activity-label">Education Centre Library(ECL)</div>
  </div>

  <ul class="activity-list" style="left:93px;">
    <li>Traditional oriental hot and cold drinks.</li>
    <li>Light snacks &amp; vegetarian dishes i.e. Koshary and Falafel</li>
    <li>Artist will use AlDar to exhibit their work</li>
    <li>A monthly entertainment event and more...</li>
  </ul>
  <ul class="activity-list" style="left:439px;">
    <li>Provide all sort of support and integration consultation through Ta3aruf</li>
    <li>Various cultural lectures with an annual planned events.</li>
    <li>Art Exhibitions. Where Artist are welcomed to use AlDar to exhibit their work</li>
    <li>Trips and Sport events for families and youth.</li>
    <li>A monthly meeting for women from different ethnics to talk about their successful integration experiences in CH.</li>
  </ul>
  <ul class="activity-list" style="left:788px;">
    <li>One-day workshop possibility for all types of adult learning</li>
    <li>Adult program courses i.e. languages, cooking, gardening, computer</li>
    <li>Intensive courses</li>
    <li>Orientation and relocation courses.</li>
    <li>Library, Book club and online magazine.</li>
  </ul>

</div>
</body>
</html>
```